Skyscraper (160x600), Banner (728x90), Banner (300x250)
Zielgruppe
Frauen zwischen 20 und 40 mit Kinderwunsch, die es auf emotionaler Ebene anzusprechen gilt
Aufgabenstellung
Wir suchen ansprechend kreativ gestaltete Werbemittel für unseren Ovulationstest FertiLUNA. Dies ist ein Urin-Schnelltest, mit dem Frauen, die schwanger werden wollen, ihre fruchtbaren Tage bestimmen können. Er funktioniert genauso wie ein Schwangerschaftstest. Die Ansprache soll sehr emotional gestaltet werden, da ein hoch emotionales Thema

```html
<!DOCTYPE html>
<html lang="de">
<head>
<meta charset="utf-8">
<title>FertiLUNA – Werbemittel 300x250</title>
<link rel="stylesheet" href="https://fonts.googleapis.com/css2?family=Libre+Bodoni:wght@400;700&family=Open+Sans:wght@700&display=swap">
<style>
  :root {
    --stage-top: #2a2d36;
    --stage-bottom: #07080b;
    --panel-bg: #ffffff;
    --panel-edge: #7ec8dc;
    --bubble-top: #ee1a88;
    --bubble-bottom: #c10868;
    --bubble-rim: #ffffff;
    --accent: #1aa6c9;
    --text-light: #ffffff;
    --photo-light: #e3f2f8;
    --photo-mid: #8fcbe0;
    --photo-deep: #3a6f8c;
  }
  * { margin: 0; padding: 0; box-sizing: border-box; }
  html, body { width: 1200px; height: 1029px; overflow: hidden; }
  body {
    background: radial-gradient(ellipse at 50% 20%, var(--stage-top), var(--stage-bottom) 75%);
    position: relative;
    font-family: "Libre Bodoni", "Times New Roman", serif;
  }
  .banner {
    position: absolute;
    width: 511px; height: 425px;
    background: var(--panel-bg);
    border: 2px solid var(--panel-edge);
    border-radius: 6px;
    overflow: hidden;
  }
  .banner--question { left: 55px; top: 51px; }
  .banner--dream    { left: 641px; top: 51px; }
  .banner--product  { left: 55px; top: 549px; }
  .banner--wish     { left: 645px; top: 549px; }

  .photo { position: absolute; }
  .photo--child {
    left: 190px; top: 0; width: 321px; height: 425px;
    background: linear-gradient(135deg, var(--photo-light), var(--photo-mid) 55%, var(--photo-deep));
  }
  .photo--mother {
    left: 230px; top: 0; width: 281px; height: 425px;
    background: linear-gradient(160deg, var(--photo-light), var(--photo-mid) 60%, #5c97b0);
  }
  .photo--belly {
    left: 250px; top: 0; width: 261px; height: 425px;
    background: linear-gradient(100deg, #ffffff, var(--photo-light) 30%, var(--photo-mid) 75%, #6aa8c2);
  }
  .product-floor {
    position: absolute; left: 0; bottom: 0; width: 511px; height: 130px;
    background: linear-gradient(180deg, rgba(255,255,255,0), #bfe4f2 60%, #7fc6df);
  }
  .photo--pack {
    left: 215px; top: 210px; width: 270px; height: 190px;
    background: linear-gradient(160deg, #f4fafd, #c8e6f2 50%, #7db9d2);
    border-radius: 6px;
  }

  .bubble {
    position: absolute; left: 10px; top: 12px;
    width: 276px; height: 410px;
    filter: drop-shadow(2px 3px 4px rgba(0,0,0,.35));
  }
  .bubble-copy {
    position: absolute; left: 10px; top: 12px; width: 266px; height: 352px;
    display: flex; flex-direction: column; align-items: center; justify-content: center;
    text-align: center; color: var(--text-light);
  }
  .copy-line { font-size: 36px; line-height: 1.15; }
  .copy-line--small { font-size: 28px; line-height: 1.2; }
  .keyword {
    font-weight: 700; color: var(--accent);
    text-shadow: 0 0 2px #fff, 0 0 2px #fff, 1px 1px 0 #fff;
    line-height: 1;
  }
  .keyword--xl { font-size: 82px; margin-top: 14px; }
  .keyword--lg { font-size: 64px; margin-top: 8px; }
  .keyword--md { font-size: 48px; margin-top: 4px; }
  .punct {
    position: absolute; color: var(--text-light); font-weight: 700;
    text-shadow: 3px 4px 5px rgba(0,0,0,.45);
    line-height: 1;
  }
  .punct--question { left: 262px; top: 150px; font-size: 170px; }
  .punct--bang { left: 250px; top: 135px; font-size: 160px; }

  .cta {
    position: absolute; left: 280px; top: 363px;
    width: 220px; height: 44px;
    border-radius: 22px;
    background: linear-gradient(180deg, var(--bubble-top), var(--bubble-bottom));
    border: 3px solid var(--bubble-rim);
    box-shadow: 0 2px 4px rgba(0,0,0,.4);
    color: var(--text-light);
    font-family: "Open Sans", Arial, sans-serif;
    font-weight: 700; font-size: 20px;
    display: flex; align-items: center; justify-content: center;
  }
</style>
</head>
<body>
  <svg width="0" height="0" style="position:absolute">
    <defs>
      <linearGradient id="bubbleFill" x1="0" y1="0" x2="0" y2="1">
        <stop offset="0" stop-color="#ee1a88"/>
        <stop offset="1" stop-color="#c10868"/>
      </linearGradient>
      <path id="bubbleShape" d="M32 4 H238 Q266 4 266 32 V324 Q266 352 238 352 H100 L52 402 L58 352 H32 Q4 352 4 324 V32 Q4 4 32 4 Z"/>
    </defs>
  </svg>

  <section class="banner banner--question">
    <div class="photo photo--child" role="img" aria-label="Foto: Kleinkind mit blauen Augen, die Hand am Mund"></div>
    <svg class="bubble" viewBox="0 0 276 410"><use href="#bubbleShape" fill="url(#bubbleFill)" stroke="#ffffff" stroke-width="6"/></svg>
    <div class="bubble-copy">
      <span class="copy-line">Wünschen</span>
      <span class="copy-line">Sie sich ein</span>
      <span class="keyword keyword--xl">Baby</span>
    </div>
    <span class="punct punct--question">?</span>
  </section>

  <section class="banner banner--dream">
    <div class="photo photo--mother" role="img" aria-label="Foto: lächelnde Mutter mit fröhlichem Baby im Arm"></div>
    <svg class="bubble" viewBox="0 0 276 410"><use href="#bubbleShape" fill="url(#bubbleFill)" stroke="#ffffff" stroke-width="6"/></svg>
    <div class="bubble-copy">
      <span class="copy-line">Träumen</span>
      <span class="copy-line">Sie nicht nur</span>
      <span class="copy-line">vom</span>
      <span class="keyword keyword--lg">Baby-<br>Glück</span>
    </div>
    <span class="punct punct--bang">!</span>
  </section>

  <section class="banner banner--product">
    <div class="product-floor"></div>
    <div class="photo photo--pack" role="img" aria-label="Produktfoto: FertiLUNA Verpackung mit Teststreifen und Becher"></div>
    <svg class="bubble" viewBox="0 0 276 410"><use href="#bubbleShape" fill="url(#bubbleFill)" stroke="#ffffff" stroke-width="6"/></svg>
    <div class="bubble-copy">
      <span class="copy-line copy-line--small">Bestimmen Sie</span>
      <span class="copy-line copy-line--small">mit FertiLUNA</span>
      <span class="copy-line copy-line--small">einfach &amp; sicher</span>
      <span class="copy-line copy-line--small">den Zeitpunkt</span>
      <span class="copy-line copy-line--small">Ihres</span>
      <span class="keyword keyword--md">Ei-<br>sprungs...</span>
    </div>
  </section>

  <section class="banner banner--wish">
    <div class="photo photo--belly" role="img" aria-label="Foto: Babybauch einer schwangeren Frau, Hände auf dem Bauch"></div>
    <svg class="bubble" viewBox="0 0 276 410"><use href="#bubbleShape" fill="url(#bubbleFill)" stroke="#ffffff" stroke-width="6"/></svg>
    <div class="bubble-copy">
      <span class="copy-line">...um Ihren</span>
      <span class="keyword keyword--lg" style="margin:14px 0 16px">Traum</span>
      <span class="copy-line">wahr zu</span>
      <span class="copy-line">machen.</span>
    </div>
    <a class="cta">HIER klicken!</a>
  </section>
</body>
</html>
```